Medical Oncologist in Rural Australia needs a Business Card

I am a medical oncologist in a regional town in Australia. I need a business card that merges a degree of conservatism (as people's lives are entrusted to me) with cutting edge (as I am always trying to understand the latest cancer biology and trying to bring new drugs to patients rapidly). I wish my card to project the idea that I am trustworthy, caring and innovative. Not overly bold colours but something that doesn't drift into the background.

Medical

```html
<!DOCTYPE html>
<html lang="en">
<head>
<meta charset="utf-8">
<title>Riverbend Medical Oncology – Business Card</title>
<link rel="stylesheet" href="https://fonts.googleapis.com/css2?family=Caladea:wght@400;700&display=swap">
<style>
  :root {
    --backdrop: #9cc3fb;
    --card: #ffffff;
    --ink: #111111;
    --brand-blue: #2251a8;
    --accent-blue: #3f6fc9;
    --rule-blue: #2b5db8;
  }
  html, body {
    margin: 0;
    width: 1200px;
    height: 900px;
    overflow: hidden;
    background: var(--backdrop);
    font-family: "Caladea", Cambria, Georgia, serif;
  }
  .card {
    position: absolute;
    left: 180px;
    top: 210px;
    width: 840px;
    height: 480px;
    background: var(--card);
    overflow: hidden;
    box-shadow: 0 10px 30px rgba(30, 60, 120, 0.25);
  }
  .rule { position: absolute; background: var(--rule-blue); }
  .rule--top { left: 560px; top: 68px; width: 280px; height: 1px; }
  .rule--top-drop { left: 560px; top: 0; width: 1px; height: 68px; }
  .rule--left { left: 0; top: 250px; width: 150px; height: 1px; }
  .rule--left-drop { left: 150px; top: 250px; width: 1px; height: 60px; }
  .rule--name { left: 150px; top: 310px; width: 690px; height: 1px; }

  .practice-name {
    position: absolute;
    left: 0;
    width: 840px;
    top: 104px;
    margin: 0;
    text-align: center;
    font-weight: 700;
    font-size: 46px;
    line-height: 54px;
    letter-spacing: 2px;
    color: var(--ink);
    text-transform: uppercase;
  }
  .doctor {
    position: absolute;
    left: 170px;
    top: 250px;
  }
  .doctor__name {
    margin: 0;
    font-size: 30px;
    line-height: 32px;
    color: var(--ink);
  }
  .doctor__credentials {
    margin: 0;
    font-size: 20px;
    line-height: 24px;
    color: var(--accent-blue);
  }
  .contact {
    position: absolute;
    display: flex;
    align-items: center;
    gap: 10px;
    font-size: 19px;
    color: var(--ink);
  }
  .contact__icon { width: 22px; height: 22px; flex: none; }
  .contact--phone { left: 170px; top: 330px; }
  .contact--email { left: 380px; top: 330px; }
  .contact--web { left: 620px; top: 330px; }
  .contact--address { left: 380px; top: 372px; }

  .band {
    position: absolute;
    left: 0;
    width: 840px;
    background: var(--brand-blue);
  }
  .band--thin { top: 414px; height: 8px; }
  .band--thick { top: 430px; height: 50px; }
</style>
</head>
<body>
  <div class="card">
    <div class="rule rule--top"></div>
    <div class="rule rule--top-drop"></div>
    <div class="rule rule--left"></div>
    <div class="rule rule--left-drop"></div>

    <h1 class="practice-name">Riverbend<br>Medical Oncology</h1>

    <div class="doctor">
      <p class="doctor__name">Jane Doe</p>
      <p class="doctor__credentials">MBBS (hons), FRACP, BE (hons)</p>
    </div>
    <div class="rule rule--name"></div>

    <div class="contact contact--phone">
      <svg class="contact__icon" viewBox="0 0 22 22"><circle cx="11" cy="11" r="11" fill="#3f6fc9"/><path d="M7.5 6.5l2 -0.5 1 2.5-1.2 1a6 6 0 0 0 3.2 3.2l1-1.2 2.5 1-0.5 2c-4.5 0.3-8.3-3.5-8-8z" fill="#fff"/></svg>
      <span>+123 456 7890</span>
    </div>
    <div class="contact contact--email">
      <svg class="contact__icon" viewBox="0 0 22 22"><circle cx="11" cy="11" r="11" fill="#3f6fc9"/><rect x="6" y="7.5" width="10" height="7" fill="none" stroke="#fff" stroke-width="1.4"/><path d="M6 7.5l5 4 5-4" fill="none" stroke="#fff" stroke-width="1.4"/></svg>
      <span>janedoe@email.com</span>
    </div>
    <div class="contact contact--web">
      <svg class="contact__icon" viewBox="0 0 22 22"><circle cx="11" cy="11" r="11" fill="#3f6fc9"/><circle cx="11" cy="11" r="5" fill="none" stroke="#fff" stroke-width="1.4"/><path d="M6 11h10M11 6c-2.5 3-2.5 7 0 10M11 6c2.5 3 2.5 7 0 10" fill="none" stroke="#fff" stroke-width="1.1"/></svg>
      <span>www.web.com</span>
    </div>
    <div class="contact contact--address">
      <svg class="contact__icon" viewBox="0 0 22 22"><circle cx="11" cy="11" r="11" fill="#3f6fc9"/><path d="M11 5.5l5.5 5h-1.6v5h-2.6v-3h-2.6v3h-2.6v-5h-1.6z" fill="#fff"/></svg>
      <span>Building, Street No, City, State, Zipcode</span>
    </div>

    <div class="band band--thin"></div>
    <div class="band band--thick"></div>
  </div>
</body>
</html>
```